An Australian based fintech company need a 12 page booklet

We need the booklet to be designed per the content attached. Can refer to a market leader for some design style inspiration - https://solvarin.com.au
Updates
I understand the briefing is somewhat confusing. I will update and extend deadline shortly. Pls pause current the design work thanks.
Need extra days to review
Please add a page prior to the Funding Option page:
How Tarudo Works:
1. Obtain a Quote
Connect with our network of reliable tradespeople to receive quotes, or bring in your preferred tradies, and we'll assist in accrediting them with Tarudo.
2. Apply for Green Funding
Apply for partial or full funding based on your quote and budget. Our straightforward, paperless application process ensures a quick turnaround, and you'll receive prompt notifications regarding your application and approval.
3. Green Home Transformation
Once your green funding is approved, coordinate with our accredited tradespeople to schedule the installation.
4. Savings Commence
After confirming the completion of the work, we'll release the full payment to your tradie. Fortnightly repayments will initiate, facilitated through either credit card or direct debit.
Target Market(s)
Australian local household
Industry/Entity Type
Green Fintech
Look and feel
Each slider illustrates characteristics of the customer's brand and the style your logo design should communicate.

```html
<!DOCTYPE html>
<html lang="en">
<head>
<meta charset="utf-8">
<title>Tarudo – Green Financing Booklet</title>
<link href="https://fonts.googleapis.com/css2?family=Montserrat:ital,wght@0,300;0,400;0,600;0,700;0,800;0,900;1,800&display=swap" rel="stylesheet">
<style>
:root{
  --navy:#1c2a44;
  --green:#2fb335;
  --green-dark:#1e8f2a;
  --green-light:#9fd8a3;
  --paper:#ffffff;
  --paper-soft:#f2f3f4;
  --ink:#3c4350;
  --muted:#8b9098;
  --stage:#e3e3e3;
  --line:#d5d8dc;
}
*{box-sizing:border-box;margin:0;padding:0}
html,body{width:1200px;height:3000px;overflow:hidden;background:var(--stage);font-family:"Montserrat",sans-serif;color:var(--ink)}
.booklet{display:flex;flex-direction:column;align-items:center;gap:25px;padding-top:25px}
.spread{width:566px;height:400px;display:flex;position:relative;box-shadow:0 6px 18px rgba(0,0,0,.18);background:var(--paper)}
.page{width:283px;height:400px;position:relative;overflow:hidden;background:var(--paper)}
.page--left{box-shadow:inset -10px 0 14px -12px rgba(0,0,0,.25)}
.page--right{box-shadow:inset 10px 0 14px -12px rgba(0,0,0,.18)}
.abs{position:absolute}
.photo{position:absolute}
.body-text{font-size:4.6px;line-height:1.55;color:var(--ink)}
.body-text p+p{margin-top:4px}
.brand{display:flex;align-items:center;gap:4px;font-weight:800;color:var(--navy);font-size:13px;letter-spacing:.5px}
.brand__mark{width:10px;height:10px;background:var(--green)}
.pill{display:inline-block;border-radius:20px;font-weight:800;color:#fff;padding:4px 12px;font-size:8.5px;letter-spacing:.4px}
.pill--navy{background:var(--navy)}
.pill--green{background:var(--green)}
.heading-green{color:var(--green);font-weight:800;font-size:8px;letter-spacing:.4px}
.icon-card{background:#fff;border-radius:5px;box-shadow:0 1px 4px rgba(0,0,0,.18);display:flex;flex-direction:column;align-items:center;justify-content:center;gap:3px;text-align:center;font-size:3.8px;font-weight:600;color:var(--navy);padding:3px}
.icon-card svg{width:13px;height:13px}
.ico{fill:none;stroke:var(--green);stroke-width:1.6;stroke-linecap:round;stroke-linejoin:round}

/* cover & disclaimer */
.disclaimer__title{top:26px;left:0;width:100%;text-align:center;color:var(--green-light);font-weight:300;font-size:17px;letter-spacing:1px}
.disclaimer__cols{top:62px;left:26px;right:26px;display:grid;grid-template-columns:1fr 1fr;gap:12px}
.disclaimer__cta{top:238px;left:40px;right:40px;text-align:center;font-size:5px;line-height:1.5;color:var(--ink)}
.contact-bar{top:268px;left:22px;right:22px;height:24px;background:var(--navy);border-radius:6px;display:flex;align-items:center;justify-content:space-around;color:#fff;font-size:5px;font-weight:600}
.contact-bar span{display:flex;align-items:center;gap:3px}
.contact-bar svg{width:7px;height:7px}
.cover__title{top:74px;left:0;width:100%;text-align:center;color:var(--navy);font-weight:900;font-size:19px;line-height:1.05}
.cover__band{top:124px;left:50%;transform:translateX(-50%);background:var(--green);color:#fff;font-weight:800;font-size:8.5px;padding:4px 12px;white-space:nowrap}

/* feature grid */
.homes-grid{top:46px;left:22px;display:grid;grid-template-columns:repeat(4,52px);gap:7px}
.homes-grid .icon-card{height:42px}
.benefit-grid{top:210px;left:22px;display:grid;grid-template-columns:repeat(4,54px);gap:7px}
.benefit-grid .icon-card{height:38px}

/* why */
.why-grid{top:30px;left:18px;right:18px;display:grid;grid-template-columns:1fr 1fr;grid-template-rows:repeat(4,82px)}
.why-cell{padding:8px;display:flex;flex-direction:column;justify-content:center}
.why-cell--grey{background:var(--paper-soft)}
.why-cell h4{font-size:6px;color:var(--navy);font-weight:800;margin-bottom:4px}
.why-cell--icon{align-items:center;justify-content:center}
.why-cell--icon svg{width:30px;height:30px}

/* table */
.options{top:18px;left:18px;width:250px;height:320px;background:#fff;box-shadow:0 2px 8px rgba(0,0,0,.2)}
.options__head{background:var(--navy);color:#fff;text-align:center;font-weight:800;font-size:10px;padding:14px 10px 10px;line-height:1.2}
.options table{width:100%;border-collapse:collapse;font-size:4.6px}
.options th,.options td{border-bottom:1px solid var(--line);padding:6px 5px;text-align:left;vertical-align:top;line-height:1.5}
.options th{color:var(--navy);font-weight:700;width:26%}
.options thead td{background:var(--green);color:#fff;font-weight:700;text-align:center}
.options__foot{top:352px;left:0;width:283px;height:20px;background:var(--green);color:#fff;font-size:5px;font-weight:700;display:flex;align-items:center;justify-content:space-between;padding:0 20px}

/* steps */
.steps__title{top:28px;left:28px;font-size:15px;font-weight:900;color:var(--navy);line-height:1;font-style:italic}
.steps{top:72px;left:28px;width:140px;display:flex;flex-direction:column;gap:12px}
.step{display:flex;gap:8px}
.step__num{color:var(--green);font-weight:900;font-style:italic;font-size:11px;width:18px;flex:none}
.step__text{font-size:4.4px;line-height:1.5}
.step__text b{color:var(--navy);display:block;font-size:5px;margin-bottom:1px}

/* transparent */
.band{position:absolute;top:0;left:0;width:566px;height:72px;background:linear-gradient(100deg,#1f9f2c,#4ccf4e 60%,#2fb335)}
.band__title{position:absolute;top:36px;left:40px;color:#fff;font-weight:800;font-size:17px;letter-spacing:7px;white-space:nowrap}
.timeline{top:150px;left:24px;width:240px}
.timeline__item{display:flex;gap:10px;margin-bottom:22px;position:relative}
.timeline__dot{width:18px;height:18px;border-radius:50%;border:1px solid var(--green);background:#fff;flex:none;display:flex;align-items:center;justify-content:center}
.timeline__dot svg{width:9px;height:9px}
.timeline__item h4{font-size:5.5px;color:var(--navy);font-weight:800;margin-bottom:2px}
.timeline__rail{top:160px;left:32.5px;width:1px;height:140px;background:var(--line)}

/* partner */
.partner__title{top:26px;left:40px;right:30px;text-align:center;font-weight:800;color:var(--navy);font-size:9px;line-height:1.25}
.perks{top:30px;left:22px;right:22px;display:flex;flex-direction:column;gap:10px}
.perk{border:1px solid var(--navy);border-radius:10px;padding:8px 12px;text-align:center}
.perk svg{width:12px;height:12px}
.perk h4{font-size:5.4px;color:var(--navy);font-weight:800;margin:2px 0 3px}
</style>
</head>
<body>
<main class="booklet">

  <!-- Spread 1: back cover & front cover -->
  <section class="spread">
    <div class="page page--left">
      <h2 class="abs disclaimer__title">DISCLAIMER</h2>
      <div class="abs disclaimer__cols body-text">
        <div>
          <p>The information in this booklet is general in nature and does not take into account your objectives, financial situation or needs. Before acting on any information you should consider its appropriateness and seek independent advice.</p>
          <p>All applications are subject to credit assessment, eligibility criteria and approval. Fees, charges and terms and conditions apply and may change without notice.</p>
        </div>
        <div>
          <p>Tarudo does not guarantee specific energy savings, which depend on usage, installation and household circumstances. Product features are indicative only and may vary between accredited tradespeople.</p>
          <p>Please read the full terms and conditions and privacy policy available online before applying for any green funding product with us.</p>
        </div>
      </div>
      <p class="abs disclaimer__cta">Contact us today to explore how Tarudo can help you make your home greener, smarter and more affordable for the years ahead.</p>
      <div class="abs contact-bar">
        <span><svg viewBox="0 0 10 10"><path class="ico" d="M2 1.5l2 .3.6 2-1 .8a6 6 0 0 0 2 2l.8-1 2 .6.3 2c-4 .5-7.5-3-6.7-6.7z"/></svg>1300 555 019</span>
        <span><svg viewBox="0 0 10 10"><rect class="ico" x="1" y="2.5" width="8" height="5.5"/><path class="ico" d="M1 2.5l4 3 4-3"/></svg>info@tarudo.co</span>
        <span><svg viewBox="0 0 10 10"><circle class="ico" cx="5" cy="5" r="4"/><path class="ico" d="M1 5h8M5 1c2 2 2 6 0 8M5 1c-2 2-2 6 0 8"/></svg>www.tarudo.co</span>
      </div>
      <div class="abs brand" style="top:330px;left:96px"><span class="brand__mark"></span>Tarudo</div>
    </div>
    <div class="page page--right">
      <div class="abs brand" style="top:36px;left:104px"><span class="brand__mark"></span>Tarudo</div>
      <h1 class="abs cover__title">INNOVATIVE<br>GREEN FINANCING</h1>
      <div class="abs cover__band">FOR SUSTAINABLE HOMES</div>
      <div class="photo" role="img" aria-label="Young seedling growing from a stack of coins in rich soil" style="top:170px;left:0;width:283px;height:230px;background:linear-gradient(180deg,#ffffff 0%,#cfe8c2 25%,#8cc57a 55%,#5b4532 85%,#3b2a1e 100%)"></div>
    </div>
  </section>

  <!-- Spread 2: sustainable homes & vision -->
  <section class="spread">
    <div class="page page--left">
      <div class="photo" role="img" aria-label="Rooftop solar panels under a bright sky" style="top:220px;left:0;width:283px;height:180px;background:linear-gradient(180deg,#ffffff 0%,#c9d0d8 40%,#6f7f93 100%)"></div>
      <div class="abs" style="top:20px;left:70px"><span class="pill pill--green">SUSTAINABLE HOMES</span></div>
      <div class="abs homes-grid">
        <div class="icon-card"><svg viewBox="0 0 14 14"><rect class="ico" x="2" y="5" width="10" height="6"/><path class="ico" d="M5 5v6M9 5v6M2 8h10"/></svg>Solar Systems</div>
        <div class="icon-card"><svg viewBox="0 0 14 14"><rect class="ico" x="3" y="3" width="8" height="9"/><path class="ico" d="M6 1.5h2M7 6v3M5.5 7.5h3"/></svg>Battery Storage</div>
        <div class="icon-card"><svg viewBox="0 0 14 14"><rect class="ico" x="4" y="2" width="6" height="10" rx="2"/><path class="ico" d="M7 5v4"/></svg>Heat Pump Hot Water</div>
        <div class="icon-card"><svg viewBox="0 0 14 14"><circle class="ico" cx="7" cy="6" r="3.5"/><path class="ico" d="M5.5 10.5h3M6 12.5h2"/></svg>LED Lighting</div>
        <div class="icon-card"><svg viewBox="0 0 14 14"><path class="ico" d="M2 7l5-4.5L12 7v5H2z"/><circle class="ico" cx="7" cy="9" r="1.3"/></svg>Smart Home Systems</div>
        <div class="icon-card"><svg viewBox="0 0 14 14"><path class="ico" d="M2 7l5-4.5L12 7v5H2zM4 9h6"/></svg>Insulation</div>
        <div class="icon-card"><svg viewBox="0 0 14 14"><rect class="ico" x="2" y="2" width="10" height="10"/><path class="ico" d="M7 2v10M2 7h10"/></svg>Double Glazing</div>
        <div class="icon-card"><svg viewBox="0 0 14 14"><rect class="ico" x="3" y="2" width="6" height="10"/><path class="ico" d="M9 5h2v5M6 5l-1 2.5h2L6 10"/></svg>EV Chargers</div>
        <div class="icon-card"><svg viewBox="0 0 14 14"><path class="ico" d="M7 2c2.5 3 4 5 4 7a4 4 0 0 1-8 0c0-2 1.5-4 4-7z"/></svg>Rainwater Harvesting</div>
        <div class="icon-card"><svg viewBox="0 0 14 14"><path class="ico" d="M3 4h8l-1 8H4zM2 4h10"/></svg>Composting Systems</div>
        <div class="icon-card"><svg viewBox="0 0 14 14"><rect class="ico" x="3" y="2" width="8" height="10" rx="1"/><circle class="ico" cx="7" cy="8" r="2"/></svg>Efficient Appliances</div>
        <div class="icon-card"><svg viewBox="0 0 14 14"><path class="ico" d="M3 4h6v3M9 7c0 1 1 2 1 3a1 1 0 0 1-2 0c0-1 1-2 1-3"/></svg>Water Fixtures</div>
        <div class="icon-card"><svg viewBox="0 0 14 14"><path class="ico" d="M7 7V13M7 7L7 2M7 7l4.5 2.5M7 7L2.5 9.5"/></svg>Wind Turbines</div>
        <div class="icon-card"><svg viewBox="0 0 14 14"><circle class="ico" cx="7" cy="7" r="5"/><path class="ico" d="M7 7l3-2M7 7l-2 3"/></svg>Ventilation</div>
        <div class="icon-card"><svg viewBox="0 0 14 14"><path class="ico" d="M2 8l5-4 5 4M3 8c1-2 3-2 4 0 1-2 3-2 4 0"/></svg>Green Roofs</div>
        <div class="icon-card"><svg viewBox="0 0 14 14"><circle class="ico" cx="7" cy="7" r="2.5"/><path class="ico" d="M7 1.5v2M7 10.5v2M1.5 7h2M10.5 7h2"/></svg>Solar Hot Water</div>
        <div class="icon-card"><svg viewBox="0 0 14 14"><rect class="ico" x="2" y="4" width="10" height="7"/><path class="ico" d="M4 11v1.5M10 11v1.5"/></svg>Air Conditioning</div>
        <div class="icon-card"><svg viewBox="0 0 14 14"><rect class="ico" x="2" y="3" width="10" height="8"/><path class="ico" d="M4 6h6M4 8h4"/></svg>Energy Monitors</div>
        <div class="icon-card"><svg viewBox="0 0 14 14"><path class="ico" d="M2 12h10M4 12V7h6v5"/></svg>Outdoor Lighting</div>
        <div class="icon-card"><svg viewBox="0 0 14 14"><path class="ico" d="M4 3h6v9H4zM6 6h2"/></svg>Pool Pumps</div>
      </div>
    </div>
    <div class="page page--right">
      <div class="photo" role="img" aria-label="Technician with a laptop inspecting solar panels on a roof" style="top:280px;left:0;width:283px;height:120px;background:linear-gradient(180deg,#ffffff 0%,#b6bfca 45%,#4f5e70 100%)"></div>
      <div class="abs brand" style="top:22px;left:150px"><span class="brand__mark"></span>Tarudo</div>
      <div class="abs body-text" style="top:50px;left:40px;width:210px;text-align:center">Tarudo is one of Australia's only dedicated green funding providers for homeowners. We partner with accredited tradespeople to make sustainable upgrades simple, affordable and accessible, so every household can enjoy a cleaner, greener home.</div>
      <div class="abs" style="top:152px;left:100px"><span class="pill pill--navy">OUR VISION</span></div>
      <div class="abs heading-green" style="top:180px;left:70px">ENVIRONMENTAL BENEFITS</div>
      <div class="abs benefit-grid">
        <div class="icon-card"><svg viewBox="0 0 14 14"><circle class="ico" cx="7" cy="7" r="4.5"/><path class="ico" d="M7 4v3l2 2"/></svg>Energy Efficiency</div>
        <div class="icon-card"><svg viewBox="0 0 14 14"><path class="ico" d="M3 9c0-3 2-5 4-5s4 2 4 5zM7 9v3"/></svg>Carbon Reduction</div>
        <div class="icon-card"><svg viewBox="0 0 14 14"><circle class="ico" cx="7" cy="7" r="2.5"/><path class="ico" d="M7 1.5v2M7 10.5v2M1.5 7h2M10.5 7h2"/></svg>Renewable Energy</div>
        <div class="icon-card"><svg viewBox="0 0 14 14"><path class="ico" d="M7 2c2.5 3 4 5 4 7a4 4 0 0 1-8 0c0-2 1.5-4 4-7z"/></svg>Water Conservation</div>
        <div class="icon-card"><svg viewBox="0 0 14 14"><path class="ico" d="M3 4h8l-1 8H4zM2 4h10"/></svg>Waste Reduction</div>
        <div class="icon-card"><svg viewBox="0 0 14 14"><rect class="ico" x="2" y="3" width="10" height="8"/><path class="ico" d="M4 6h6M4 8h4"/></svg>Lower Utility Bills</div>
        <div class="icon-card"><svg viewBox="0 0 14 14"><circle class="ico" cx="7" cy="7" r="5"/><path class="ico" d="M7 4v6M5 5.5h3a1 1 0 0 1 0 2H6a1 1 0 0 0 0 2h3"/></svg>Long-Term Savings</div>
        <div class="icon-card"><svg viewBox="0 0 14 14"><path class="ico" d="M7 12L2.5 7.5a2.5 2.5 0 0 1 4.5-3 2.5 2.5 0 0 1 4.5 3z"/></svg>Healthier Living</div>
      </div>
    </div>
  </section>

  <!-- Spread 3: why Tarudo -->
  <section class="spread">
    <div class="page page--left">
      <div class="abs" style="top:24px;left:110px"><span class="pill pill--navy">WHY TARUDO</span></div>
      <p class="abs body-text" style="top:50px;left:60px;width:190px;text-align:center">Tarudo is more than a financing option; we're your dedicated partner in making your home a beacon of sustainability.</p>
      <div class="photo" role="img" aria-label="Smiling family sitting beside solar panels on their rooftop" style="top:80px;left:0;width:283px;height:320px;background:linear-gradient(180deg,#ffffff 0%,#a9b9c4 20%,#6f8a6a 55%,#3e4c5c 100%)"></div>
    </div>
    <div class="page page--right">
      <div class="abs why-grid">
        <div class="why-cell">
          <h4>Comprehensive Funding Solutions</h4>
          <p class="body-text">From solar panels to batteries and efficient appliances, we fund a wide range of green upgrades for your home.</p>
        </div>
        <div class="why-cell why-cell--grey why-cell--icon"><svg viewBox="0 0 30 30"><circle class="ico" cx="15" cy="15" r="6"/><path class="ico" d="M15 3v5M15 22v5M3 15h5M22 15h5M7 7l3 3M20 20l3 3M23 7l-3 3M7 23l3-3"/></svg></div>
        <div class="why-cell why-cell--grey why-cell--icon"><svg viewBox="0 0 30 30"><rect class="ico" x="5" y="6" width="14" height="18"/><path class="ico" d="M8 11h8M8 15h8M8 19h5M20 18l3 3 5-6"/></svg></div>
        <div class="why-cell">
          <h4>Streamlined Approval Process</h4>
          <p class="body-text">Our paperless online application is quick and easy, with clear updates at every step of your approval.</p>
        </div>
        <div class="why-cell">
          <h4>Flexible Repayment Terms</h4>
          <p class="body-text">Choose fortnightly repayments that suit your budget, paid by credit card or direct debit.</p>
        </div>
        <div class="why-cell why-cell--grey why-cell--icon"><svg viewBox="0 0 30 30"><circle class="ico" cx="15" cy="15" r="10"/><path class="ico" d="M15 8v14M11 11h6a2.5 2.5 0 0 1 0 5h-4a2.5 2.5 0 0 0 0 5h6"/></svg></div>
        <div class="why-cell why-cell--grey why-cell--icon"><svg viewBox="0 0 30 30"><circle class="ico" cx="15" cy="16" r="10"/><path class="ico" d="M15 10v6l4 3M12 3h6"/></svg></div>
        <div class="why-cell">
          <h4>Quick Turnaround</h4>
          <p class="body-text">Receive a fast decision so your green home transformation can begin without unnecessary delays.</p>
        </div>
      </div>
    </div>
  </section>

  <!-- Spread 4: funding options -->
  <section class="spread">
    <div class="page page--left" style="background:var(--paper-soft)">
      <div class="photo" role="img" aria-label="Green leafy background fading behind the table" style="top:0;left:0;width:283px;height:60px;background:linear-gradient(180deg,#2f8a3a,#eef2ee)"></div>
      <div class="photo" role="img" aria-label="Dark soil along the bottom of the page" style="top:330px;left:0;width:283px;height:70px;background:linear-gradient(180deg,#6b5440,#3a2b20)"></div>
      <div class="abs options">
        <div class="options__head">TARUDO GREEN FUNDING<br>OPTIONS</div>
        <table>
          <thead><tr><td></td><td>Green Loan</td><td>Green Loan Plus</td></tr></thead>
          <tbody>
            <tr><th>Funding Type</th><td>Unsecured personal loan for eligible sustainable home upgrades</td><td>Larger loan for whole-of-home energy upgrades</td></tr>
            <tr><th>Loan Amount</th><td>$2,000 – $30,000</td><td>$30,001 – $50,000</td></tr>
            <tr><th>Repayment Period</th><td>6 months – 84 months</td><td>12 months – 10 years</td></tr>
            <tr><th>Eligibility &amp; Terms</th><td>Australian homeowners aged 18+ with regular income</td><td>Subject to credit assessment and approval</td></tr>
          </tbody>
        </table>
      </div>
      <div class="abs options__foot"><span>Fees &amp; charges apply</span><span>Apply at www.tarudo.co</span></div>
    </div>
    <div class="page page--right">
      <div class="photo" role="img" aria-label="Hand placing a coin beside seedlings growing from coin stacks in soil" style="top:0;left:0;width:283px;height:400px;background:linear-gradient(160deg,#e6ece4 0%,#9fbf8c 35%,#5b7d44 60%,#6d5641 80%,#3d2d22 100%)"></div>
    </div>
  </section>

  <!-- Spread 5: how Tarudo works -->
  <section class="spread">
    <div class="page page--left">
      <h2 class="abs steps__title">HOW TARUDO<br>WORKS</h2>
      <div class="abs steps">
        <div class="step"><span class="step__num">01</span><p class="step__text"><b>Obtain a Quote</b>Connect with our network of reliable tradespeople to receive quotes, or bring in your preferred tradies, and we'll assist in accrediting them with Tarudo.</p></div>
        <div class="step"><span class="step__num">02</span><p class="step__text"><b>Apply for Green Funding</b>Apply for partial or full funding based on your quote and budget. Our straightforward, paperless application process ensures a quick turnaround.</p></div>
        <div class="step"><span class="step__num">03</span><p class="step__text"><b>Green Home Transformation</b>Once your green funding is approved, coordinate with our accredited tradespeople to schedule the installation.</p></div>
        <div class="step"><span class="step__num">04</span><p class="step__text"><b>Savings Commence</b>After confirming completion of the work, we'll release full payment to your tradie. Fortnightly repayments initiate by credit card or direct debit.</p></div>
      </div>
      <div class="photo" role="img" aria-label="Soft desk scene with glasses fading in from the right" style="top:0;left:175px;width:108px;height:400px;background:linear-gradient(90deg,rgba(255,255,255,1),#d9d9d9 60%,#b8b8b8)"></div>
    </div>
    <div class="page page--right">
      <div class="photo" role="img" aria-label="Hand holding a light bulb with a small plant inside, surrounded by eco icons" style="top:0;left:0;width:283px;height:400px;background:linear-gradient(135deg,#bdbdbd 0%,#8e8e8e 40%,#3f4148 70%,#9ea39a 100%)"></div>
    </div>
  </section>

  <!-- Spread 6: simple and transparent -->
  <section class="spread">
    <div class="band"></div>
    <div class="band__title" style="z-index:2">SIMPLE AND TRANSPARENT</div>
    <div class="page page--left" style="background:transparent">
      <p class="abs body-text" style="top:84px;left:24px;width:235px">With Tarudo, your journey to a greener home is not only straightforward but also tailored to your unique circumstances. We believe that simplicity and transparency are key, so we assess every application fairly using three clear criteria.</p>
      <div class="abs timeline__rail"></div>
      <div class="abs timeline">
        <div class="timeline__item"><span class="timeline__dot"><svg viewBox="0 0 10 10"><path class="ico" d="M1 5l4-3.5L9 5v4H1z"/></svg></span><div><h4>Home Ownership</h4><p class="body-text">You must own or be purchasing the property where the green upgrade will be installed.</p></div></div>
        <div class="timeline__item"><span class="timeline__dot"><svg viewBox="0 0 10 10"><circle class="ico" cx="5" cy="5" r="3.5"/><path class="ico" d="M5 5l2-1.5"/></svg></span><div><h4>Credit Score</h4><p class="body-text">We review your credit history to ensure repayments are manageable and responsible.</p></div></div>
        <div class="timeline__item"><span class="timeline__dot"><svg viewBox="0 0 10 10"><path class="ico" d="M2 5l2 2 4-4"/></svg></span><div><h4>Service Ability</h4><p class="body-text">Your income and expenses are considered to confirm you can comfortably meet repayments.</p></div></div>
      </div>
    </div>
    <div class="page page--right" style="background:transparent">
      <p class="abs body-text" style="top:84px;left:20px;width:240px">We believe that your eligibility should be assessed on a fair and comprehensive evaluation, making access to sustainable living easier for every Australian household.</p>
      <div class="photo" role="img" aria-label="Installer holding a solar panel while business partners shake hands outdoors" style="top:130px;left:0;width:283px;height:270px;background:linear-gradient(180deg,#ffffff 0%,#d8dcd6 25%,#6f7a72 65%,#2f3540 100%)"></div>
    </div>
  </section>

  <!-- Spread 7: vendor & partner -->
  <section class="spread">
    <div class="page page--left">
      <h2 class="abs partner__title">ON BOARD AS A TARUDO<br>VENDOR &amp; PARTNER</h2>
      <p class="abs body-text" style="top:56px;left:50px;width:200px;text-align:center">Becoming a Tarudo vendor positions you at the forefront of sustainable innovation, offering a unique opportunity to contribute to environmental conservation while expanding your business horizons.</p>
      <div class="photo" role="img" aria-label="Two partners shaking hands in front of a solar farm" style="top:100px;left:0;width:283px;height:300px;background:linear-gradient(180deg,#ffffff 0%,#c4d2de 25%,#6f8aa3 60%,#3d4e3f 100%)"></div>
    </div>
    <div class="page page--right">
      <div class="abs perks">
        <div class="perk"><svg viewBox="0 0 14 14"><path class="ico" d="M2 11l4-4 2 2 4-5M9 4h3v3"/></svg><h4>Expanding Opportunities<br>Competitive Rates and Transparent Fee Structures</h4><p class="body-text">Access new customers with clear pricing and no hidden costs for you or your clients.</p></div>
        <div class="perk"><svg viewBox="0 0 14 14"><rect class="ico" x="2" y="4" width="10" height="7"/><path class="ico" d="M5 4V2.5h4V4"/></svg><h4>Enhanced Sales Advantage<br>Flexible Funding Options to Boost Sales</h4><p class="body-text">Offer customers flexible green funding that helps convert more quotes into confirmed jobs.</p></div>
        <div class="perk"><svg viewBox="0 0 14 14"><circle class="ico" cx="7" cy="7" r="5"/><path class="ico" d="M7 4v3l2 2"/></svg><h4>Streamlined Operations<br>Paperless Applications and Rapid Approvals</h4><p class="body-text">Our digital process keeps paperwork minimal so you can focus on installations.</p></div>
        <div class="perk"><svg viewBox="0 0 14 14"><path class="ico" d="M3 7.5l2.5 2.5L11 4"/></svg><h4>Exclusive Perks<br>Instant Payments for Completed Installations</h4><p class="body-text">Receive full payment once work is confirmed complete, keeping your cash flow healthy.</p></div>
      </div>
    </div>
  </section>

</main>
</body>
</html>
```